Yard sign design for high end luxury home builder.

Need a design for signage on custom homes that are being built. I already have a logo that I am satisfied with that needs to be incorporated. I need the following incorporated in the design of the sign-
- Lic number 318562
- phone number (555) 271-4038
- pendrickhomeworks.com
- Logo/Branding

If possible it may be nice to have the following quote that is on are business cards-

Quote from Osmund of Veltarra-
HE WHO WORKS WITH HIS HANDS IS A LABORER.
HE WHO WORKS WITH HIS HANDS & HIS HEAD IS A CRAFTSMAN.
HE WHO WORKS WITH HIS HANDS & HIS HEAD & HIS HEART IS AN ARTISAN.
-OSMUND OF VELTARRA

Target Market(s)

Archetect, Designers, Clients desiring to build a new home or remodel.

Colors
fde9d4
fee4d5
fabb94
fac994
faa54b
f68d4d
f37122
f78f20
f68e4e

Requirements
Must have
• - Lic number 318562
• - phone number (555) 271-4038
• - pendrickhomeworks.com
• - Logo/Branding
Nice to have
• Quote from Osmund of Veltarra-
• HE WHO WORKS WITH HIS HANDS IS A LABORER.
• HE WHO WORKS WITH HIS HANDS & HIS HEAD IS A CRAFTSMAN.
• HE WHO WORKS WITH HIS HANDS & HIS HEAD & HIS HEART IS AN ARTISAN.
• -OSMUND OF VELTARRA
• OR the below statement-
• Craftsmen that Care
Should not have
• Any additional verbiage not specified above including any type of verbiage about what kind of company we are. For instance- Integrity, reputable... It's just all played out. Im just looking for a bitching design that has the info that compliments my logo/branding.

```html
<!DOCTYPE html>
<html lang="en">
<head>
<meta charset="utf-8">
<title>Pendrick Homeworks – Yard Sign</title>
<link rel="stylesheet" href="https://fonts.googleapis.com/css2?family=Source+Sans+3:wght@600;700&family=Cabin:wght@400;500&family=Archivo+Black&display=swap">
<style>
  :root {
    --backdrop: #e8e9ea;
    --wood: #5b4333;
    --wood-dark: #46332a;
    --tan: #a88b6a;
    --ink: #4a3627;
    --paper: #ffffff;
  }
  * { margin: 0; padding: 0; box-sizing: border-box; }
  html, body { width: 1200px; height: 843px; overflow: hidden; background: var(--backdrop); }
  .canvas { position: relative; width: 1200px; height: 843px; }

  .sign {
    position: absolute; left: 64px; top: 64px; width: 1071px; height: 713px;
    background: var(--paper);
    box-shadow: 0 6px 14px rgba(0,0,0,0.25);
    overflow: hidden;
  }
  .sign-shapes { position: absolute; inset: 0; }

  .brand-panel {
    position: absolute; left: 45px; top: 0; width: 317px; height: 357px;
    background: var(--paper);
    display: flex; flex-direction: column; align-items: center; justify-content: center;
    gap: 22px;
  }
  .brand-mark { width: 96px; height: 96px; background: var(--tan); }
  .brand-name {
    font-family: "Archivo Black", sans-serif; color: var(--tan);
    text-align: center; line-height: 1.05; letter-spacing: 1px;
  }
  .brand-name .line1 { display: block; font-size: 44px; }
  .brand-name .line2 { display: block; font-size: 27px; letter-spacing: 2px; }
  .brand-rule { position: absolute; left: 45px; top: 370px; width: 317px; height: 10px; background: var(--tan); }

  .quote {
    position: absolute; right: 58px; top: 43px;
    font-family: "Source Sans 3", sans-serif; font-weight: 700;
    font-size: 68px; line-height: 87px; color: var(--paper);
    text-align: right; text-transform: uppercase; white-space: nowrap;
    text-shadow: 3px 4px 6px rgba(0,0,0,0.45);
  }
  .quote-author {
    position: absolute; right: 64px; top: 412px;
    font-family: "Source Sans 3", sans-serif; font-weight: 700;
    font-size: 33px; color: var(--paper); white-space: nowrap;
    text-shadow: 2px 3px 5px rgba(0,0,0,0.45);
  }

  .phone {
    position: absolute; left: 45px; top: 507px;
    font-family: "Source Sans 3", sans-serif; font-weight: 700;
    font-size: 82px; line-height: 1; color: var(--ink); white-space: nowrap;
  }
  .website {
    position: absolute; left: 46px; top: 612px; width: 533px; height: 40px;
    border: 2px solid var(--tan);
    font-family: "Cabin", sans-serif; font-size: 34px; line-height: 36px;
    color: var(--ink); text-align: center; letter-spacing: 0.5px; white-space: nowrap;
  }
  .license {
    position: absolute; right: 64px; top: 610px;
    font-family: "Cabin", sans-serif; font-weight: 500; font-size: 36px;
    color: var(--ink); letter-spacing: 0.5px; white-space: nowrap;
  }
</style>
</head>
<body>
<div class="canvas">
  <div class="sign">
    <svg class="sign-shapes" width="1071" height="713" viewBox="0 0 1071 713">
      <g role="img" aria-label="Weathered dark wood plank texture">
        <polygon points="0,0 1071,0 1071,530 646,530 601,482 0,482" fill="var(--wood)"/>
      </g>
      <polygon points="556,482 601,482 646,530 604,530" fill="var(--tan)"/>
      <rect x="0" y="699" width="1071" height="14" fill="var(--wood-dark)"/>
    </svg>

    <div class="brand-panel">
      <div class="brand-mark"></div>
      <div class="brand-name"><span class="line1">PENDRICK</span><span class="line2">HOMEWORKS</span></div>
    </div>
    <div class="brand-rule"></div>

    <blockquote class="quote">“He who works<br>with his hands<br>&amp; his head<br>is a craftsman”</blockquote>
    <p class="quote-author">-OSMUND OF VELTARRA</p>

    <p class="phone">(555) 271-4038</p>
    <p class="website">www.pendrickhomeworks.com</p>
    <p class="license">Lic number 318562</p>
  </div>
</div>
</body>
</html>
```